Creative Report - A Presentation

We are looking for a report to visual workers' compensation claim data and the impact claims have on premium. I’m looking for something that is very visually new, appealing, easy to understand, and cutting edge.

Right now we are looking for 6 pages to be designed: a cover page, an informative page, and 4 reports. The key data for the last 3 reports are listed in the other document attached named “Key Data for Report”. These should be designed in a 8.5 x 11 page layout.

I would prefer a way where things can be combined without looking too crowded. You can play around with the background, for printing purposes try to leave white space.

Attached are a few graphs that I found that I like the look of. Please design when YOU think is best. The docx & the comments on the side are just to help you visualize.

We are a mod analysis company that is always developing new reports. We are hoping to find a designer we can work with in the future as well – think of this as a trial run!

2 designers reached out this morning wanting to submit designs, I would like to see what they have.

```html
<!DOCTYPE html>
<html lang="en">
<head>
<meta charset="utf-8">
<title>Workers Compensation Executive Summary</title>
<link href="https://fonts.googleapis.com/css2?family=Montserrat:wght@400;500;600;700;800&family=Rubik:wght@500;600;700&display=swap" rel="stylesheet">
<style>
:root{
  --navy:#0d1b6e;
  --navy-dark:#0a1558;
  --gold:#f9ac2a;
  --gold-deep:#e39a12;
  --ink:#222;
  --muted:#555;
  --rule:#cfcfcf;
  --panel:#efefef;
  --stage:#cfcfcf;
  --th:#8a8a8a;
}
*{margin:0;padding:0;box-sizing:border-box}
html,body{width:1200px;height:2302px;overflow:hidden}
body{background:var(--stage);font-family:"Montserrat",sans-serif;color:var(--ink);position:relative}
.page{position:absolute;width:489px;height:632px;background:#fff;overflow:hidden;box-shadow:0 3px 10px rgba(0,0,0,.18)}
.p1{left:71px;top:119px;background:linear-gradient(160deg,#f1f1f1 0%,#fbfbfb 40%,#fff 65%)}
.p2{left:633px;top:119px}
.p3{left:71px;top:825px}
.p4{left:633px;top:825px}
.p5{left:71px;top:1524px}
.p6{left:633px;top:1524px}
.abs{position:absolute}

.brand{position:absolute;display:flex;align-items:center;gap:6px}
.brand-square{width:26px;height:26px;border:4px solid var(--navy);border-radius:3px;flex:none}
.brand-name{font-weight:800;color:var(--navy-dark);font-size:7.2px;line-height:1.15;text-transform:uppercase}
.brand.large .brand-square{width:50px;height:50px;border-width:7px}
.brand.large .brand-name{font-size:14px}
.brand{left:37px;top:32px}

.bottom-band{position:absolute;left:0;bottom:0;width:100%;height:8px;background:var(--navy)}
.footer-note{position:absolute;left:37px;top:585px;width:400px;font-size:5.6px;line-height:1.3;color:var(--muted)}
.page-num{position:absolute;left:441px;top:586px;width:18px;height:18px;border-radius:50%;background:var(--navy);color:#fff;font-size:6px;font-weight:700;display:flex;align-items:center;justify-content:center;box-shadow:0 0 0 2px #c9cfe8}
.page-rule{position:absolute;left:37px;width:416px;height:1px;background:var(--rule)}

.section-tab{position:absolute;left:37px;height:18px;padding:0 24px 0 14px;background:var(--navy);color:#fff;font-weight:700;font-size:11.5px;letter-spacing:.6px;line-height:18px;clip-path:polygon(0 0,100% 0,calc(100% - 10px) 100%,0 100%)}
.body-text{position:absolute;left:37px;width:420px;font-size:7px;line-height:1.35;color:#333}
.photo{position:absolute}

/* cover */
.cover-title{position:absolute;left:63px;top:341px;font-family:"Rubik",sans-serif;font-weight:700;font-size:36px;line-height:1.1;color:#111}
.cover-title .accent{color:var(--navy)}
.cover-bar{position:absolute;left:39px;top:345px;width:5px;height:108px;background:var(--navy)}
.cover-mod{position:absolute;left:39px;top:468px;width:387px;height:29px;background:var(--gold);font-family:"Rubik",sans-serif;font-weight:600;font-size:22px;color:#1a1a1a;text-align:center;line-height:29px}
.cover-field{position:absolute;font-size:9px;color:#444;display:flex;align-items:flex-end;gap:6px}
.cover-field .line{border-bottom:1px solid #999;height:1px;margin-bottom:2px}
.cover-note{left:39px;top:578px;width:390px}
.cover-band{position:absolute;left:0;bottom:0;width:100%;height:17px}

/* page 2 */
.they-tab{position:absolute;left:37px;top:117px;width:110px;height:18px;background:var(--gold);color:#fff;font-weight:700;font-size:11px;line-height:18px;padding-left:14px;letter-spacing:.5px;clip-path:polygon(0 0,100% 0,calc(100% - 8px) 100%,0 100%)}
.they-box{position:absolute;left:37px;top:135px;width:416px;height:73px;background:var(--navy);padding:11px 14px;display:grid;grid-template-columns:190px 1fr;row-gap:5px;column-gap:0}
.tick-item{display:flex;gap:6px;color:#fff;font-size:7.4px;font-weight:600;line-height:1.05}
.tick{flex:none;width:8px;height:8px;border-radius:50%;background:var(--gold);position:relative;margin-top:0}
.tick::after{content:"";position:absolute;left:2.3px;top:1.4px;width:2px;height:3.6px;border:solid #fff;border-width:0 1.2px 1.2px 0;transform:rotate(45deg)}
.osha{position:absolute;left:37px;top:220px;font-size:8.5px;font-weight:700;color:var(--navy);line-height:1.35}
.osha span{color:#111}
.dark-bullets{position:absolute;left:37px;top:288px;width:420px;display:grid;grid-template-columns:210px 1fr;row-gap:8px}
.dark-bullets .tick-item{color:#111;font-size:7.3px;font-weight:700}

/* page 3 */
.exp-title{position:absolute;left:204px;top:36px;font-family:"Rubik",sans-serif;font-weight:700;font-size:19.5px;color:var(--navy);letter-spacing:.3px}
.exp-title span{color:var(--gold)}
.slider{position:absolute;left:37px;top:276px;width:421px;height:14px;border-radius:7px;background:#d9d9d9}
.slider-fill{position:absolute;left:74px;top:3px;width:252px;height:8px;background:var(--navy)}
.slider-tick{position:absolute;left:205px;top:0;width:1px;height:14px;background:#aaa}
.knob{position:absolute;width:16px;height:16px;border-radius:50%;top:-1px;border:2px solid #fff;box-shadow:0 0 0 1px #bbb}
.knob.min{left:66px;background:var(--gold)}
.knob.actual{left:318px;background:var(--navy)}
.slider-label{position:absolute;font-size:7px;font-weight:700;text-align:center;line-height:1.2}
.explain-box{position:absolute;left:37px;top:338px;width:422px;height:132px;background:var(--panel)}
.explain-box .section-tab{left:0;top:0;font-size:11px}
.explain-row{position:absolute;left:17px;width:390px;font-size:6.9px;line-height:1.35;color:#333;padding-bottom:6px}
.explain-row.ruled{border-bottom:1px solid var(--rule)}
.summary-h{position:absolute;left:37px;top:488px;font-size:10.5px;font-weight:700;letter-spacing:.4px}

/* page 4 */
.stats{position:absolute;left:37px;top:180px;width:421px;height:71px;background:var(--navy);display:grid;grid-template-columns:1fr 1fr 1fr}
.stat{color:#fff;text-align:center;padding-top:24px;font-size:7px;line-height:1.3;position:relative}
.stat:nth-child(2){background:var(--navy-dark)}
.stat b{display:block;font-size:11px;font-weight:700}
.stat-icon{position:absolute;left:50%;top:-19px;transform:translateX(-50%);width:34px;height:34px;border-radius:50%;background:radial-gradient(circle at 40% 35%,#fdc64d,var(--gold-deep));border:2px solid #fff;display:flex;align-items:center;justify-content:center}
.sub-h{position:absolute;left:0;width:100%;text-align:center;font-size:11px;font-weight:700;letter-spacing:.4px;color:#111}
.chart-panel{position:absolute;left:37px;width:421px;background:var(--panel)}
.donut-label{position:absolute;font-size:6.9px;line-height:1.75;color:#222}
.donut-label h4{font-size:6.8px;font-weight:700;letter-spacing:.3px}
.legend{position:absolute;font-size:6.9px;font-weight:700;display:flex;align-items:center;gap:5px;letter-spacing:.3px}
.legend i{width:6px;height:6px;display:block}

/* tables */
.data-table{position:absolute;left:37px;width:421px;border-collapse:collapse;font-size:6.4px;color:#333;border-radius:6px;overflow:hidden}
.data-table th{background:var(--th);color:#fff;font-weight:700;font-size:6.6px;letter-spacing:.2px;height:18px;text-transform:uppercase;border-right:1px solid #fff;white-space:nowrap}
.data-table th:last-child{border-right:none}
.data-table td{text-align:center;border-right:1px solid #fff}
.data-table td:last-child{border-right:none}
.data-table tbody tr:nth-child(odd) td{background:#f3f3f3}
.data-table tbody tr:nth-child(even) td{background:#e6e6e6}
.pie-label{position:absolute;font-size:5.8px;font-weight:600}
</style>
</head>
<body>

<!-- Page 1: cover -->
<section class="page p1">
  <div class="brand large" style="left:39px;top:51px">
    <span class="brand-square"></span>
    <span class="brand-name">Workers Compensation<br>Executive Summary</span>
  </div>
  <div class="cover-bar"></div>
  <h1 class="cover-title">WORKERS<br><span class="accent">COMPENSATION</span><br>EXECUTIVE SUMMARY</h1>
  <div class="cover-mod">Mod Effective 10-08-2022</div>
  <div class="cover-field" style="left:39px;top:514px">Name of agent <span class="line" style="width:310px"></span></div>
  <div class="cover-field" style="left:39px;top:549px">Phone no. <span class="line" style="width:130px"></span>&nbsp; Email <span class="line" style="width:165px"></span></div>
  <p class="footer-note cover-note">Proprietary and Confidential. Rate Insight provides for an ESTIMATE of an experience modification factor. Your official experience modification factor is issued solely by the applicable workers' compensation rating bureau. Rate Insight Inc. All Rights Reserved.</p>
  <svg class="cover-band" viewBox="0 0 489 17" preserveAspectRatio="none">
    <path d="M0 17V3H390C420 3 425 8 436 17Z" fill="#0d1b6e"/>
    <path d="M395 0C425 0 433 7 447 17H438C427 8 420 3 392 3Z" fill="#f9ac2a"/>
  </svg>
</section>

<!-- Page 2: informative -->
<section class="page p2">
  <div class="brand"><span class="brand-square"></span><span class="brand-name">Workers Compensation<br>Executive Summary</span></div>
  <p class="body-text" style="top:76px">Workers compensation claims can have a significant impact on a business. In addition to the direct claim costs, there are many other costs associated with a workers compensation claim that can impact a business.</p>
  <div class="they-tab">THEY ARE</div>
  <div class="they-box">
    <div class="tick-item"><i class="tick"></i>Work Comp Premium Costs</div>
    <div class="tick-item"><i class="tick"></i>Lost Opportunities due to staffing</div>
    <div class="tick-item"><i class="tick"></i>Overtime</div>
    <div class="tick-item"><i class="tick"></i>Lost Productivity</div>
    <div class="tick-item"><i class="tick"></i>Administrative time spent on<br>claim after an injury</div>
    <div class="tick-item"><i class="tick"></i>Clean up or repair of damaged<br>equipment</div>
  </div>
  <p class="osha">OSHA estimates that depending upon the size of the claim indirect<br><span>costs range from 1 to 4 times the direct costs.</span></p>
  <p class="body-text" style="top:247px">Workers compensation claims can have a significant impact on a business. In addition to the direct claim costs, there are many other costs associated with a workers compensation claim that can impact a business.</p>
  <div class="dark-bullets">
    <div class="tick-item"><i class="tick"></i>A medical only claim is reduced by<br>70% in the mod calculation.</div>
    <div class="tick-item" style="grid-row:span 2"><i class="tick"></i>All claims are also limited by a primary<br>threshold value where claims are<br>grouped into primary claims and<br>excess claims.</div>
    <div class="tick-item"><i class="tick"></i>A medical/indemnity claim has<br>no reduction.</div>
  </div>
  <p class="body-text" style="top:344px">The following report will analyze the types of claims that are occurring in your business and will group them together for ease of identifying trends and areas of opportunity to improve.</p>
  <p class="body-text" style="top:373px">By identifying the types and causes of losses many times a cost/benefit analysis can be performed to allow for safety training, additional equipment or building or process improvements.</p>
  <p class="body-text" style="top:402px">For the premium cost analysis in this report we have used a manual premium of $XXX,XXX. A manual premium is the premium derived by the carrier before any credits, debits, or experience rating.</p>
  <div class="photo" role="img" aria-label="Photo of staff working at desks in a bright open-plan office" style="left:37px;top:423px;width:407px;height:147px;background:linear-gradient(180deg,#fff 0%,#e6e6e6 25%,#b9b4ad 60%,#6b6761 100%)"></div>
  <p class="footer-note">Proprietary and Confidential. Rate Insight provides for an ESTIMATE of an experience modification factor. Your official experience modification factor is issued solely by the applicable workers' compensation rating bureau. Rate Insight Inc. All Rights Reserved.</p>
  <div class="page-num">02</div>
  <div class="bottom-band"></div>
</section>

<!-- Page 3: experience mod -->
<section class="page p3">
  <div class="brand"><span class="brand-square"></span><span class="brand-name">Workers Compensation<br>Executive Summary</span></div>
  <h2 class="exp-title"><span>YOUR</span> EXPERIENCE MOD</h2>
  <div class="photo" role="img" aria-label="Photo of a business handshake over a city skyline" style="left:38px;top:81px;width:421px;height:140px;border:2px solid #e4e4e4;background:linear-gradient(90deg,#6f8592 0%,#a9b9c2 35%,#e9d8c4 52%,#a8b8c3 68%,#6e8494 100%)"></div>
  <div class="page-rule" style="top:239px;width:421px"></div>
  <div class="slider-label" style="left:294px;top:254px">Actual Mod<br>1.19</div>
  <div class="slider">
    <div class="slider-fill"></div>
    <div class="slider-tick"></div>
    <div class="knob min"></div>
    <div class="knob actual"></div>
  </div>
  <div class="slider-label" style="left:56px;top:296px">0.63<br>Min Mod</div>
  <div class="page-rule" style="top:321px;width:421px"></div>
  <div class="explain-box">
    <div class="section-tab">MOD VALUE EXPLANATION</div>
    <p class="explain-row ruled" style="top:33px">A mod value below 1.0 means your company is performing better than your peers. If your company had no claims your lowest possible mod value would be 0.632</p>
    <p class="explain-row ruled" style="top:74px">A mod of 1.0 is considered average.</p>
    <p class="explain-row" style="top:103px">A mod value above 1.0 means your company is performing worse than your peers and you pay more in workers compensation premium.</p>
  </div>
  <h3 class="summary-h">SUMMARY</h3>
  <p class="body-text" style="top:508px">The incurred claims reported have a claim impact of .56 on your mod value. This is increasing your premium annually by $112,000.</p>
  <p class="body-text" style="top:537px">In the following pages we'll dig into the types of claims your business is having and look for areas of opportunity to reduce or eliminate claims and lower your mod value.</p>
  <div class="page-rule" style="top:569px;width:421px"></div>
  <p class="footer-note">Proprietary and Confidential. Rate Insight provides for an ESTIMATE of an experience modification factor. Your official experience modification factor is issued solely by the applicable workers' compensation rating bureau. Rate Insight Inc. All Rights Reserved.</p>
  <div class="page-num">03</div>
  <div class="bottom-band"></div>
</section>

<!-- Page 4: medical vs medical/indemnity -->
<section class="page p4">
  <div class="brand"><span class="brand-square"></span><span class="brand-name">Workers Compensation<br>Executive Summary</span></div>
  <div class="section-tab" style="top:74px">MEDICAL VS MEDICAL/INDEMNITY CLAIMS</div>
  <p class="body-text" style="top:98px;width:421px;text-align:justify">The type of claims your business is having can have a significant impact on your mod value as not all claims are valued equally. Medical only claims have their value reduced by 70% in the mod calculation and any claim with an indemnity payment is not reduced. This is one of the reasons an effective return to work program can help reduce your premium costs.</p>
  <p class="abs" style="left:37px;top:144px;font-size:8.4px;font-weight:700">Here's your company's breakdown</p>
  <div class="stats">
    <div class="stat"><span class="stat-icon"><svg width="14" height="14" viewBox="0 0 14 14"><rect x="2" y="2" width="10" height="10" rx="2" fill="none" stroke="#fff" stroke-width="1.3"/><path d="M7 4v6M5 6h4" stroke="#fff" stroke-width="1.3"/></svg></span>The total losses for the<br>period reviewed are<b>$284,623</b></div>
    <div class="stat"><span class="stat-icon"><svg width="14" height="14" viewBox="0 0 14 14"><path d="M7 2v10M2 7h10" stroke="#fff" stroke-width="2.2"/></svg></span>Medical only claims<br>accounted for<b>$85,719</b>in losses</div>
    <div class="stat"><span class="stat-icon"><svg width="14" height="14" viewBox="0 0 14 14"><circle cx="5" cy="5" r="3" fill="none" stroke="#fff" stroke-width="1.3"/><circle cx="9.5" cy="9.5" r="2.5" fill="none" stroke="#fff" stroke-width="1.3"/></svg></span>Medical/Indemnity claims<br>accounts for<b>$198,904</b>in losses</div>
  </div>
  <h3 class="sub-h" style="top:263px">MEDICAL ONLY VS MEDICAL/INDEMNITY CLAIMS</h3>
  <div class="chart-panel" style="top:287px;height:167px">
    <div class="donut-label" style="left:18px;top:14px;text-align:right;width:137px">
      <h4 style="color:var(--navy);text-align:left">MEDICAL/INDEMNITY CLAIMS</h4>
      $198,904 incurred losses<br>0.446 mod impact<br>$267,600 3yr premium impact
    </div>
    <div class="donut-label" style="left:277px;top:14px">
      <h4 style="color:var(--gold-deep)">MEDICAL ONLY CLAIMS</h4>
      $85,719 incurred losses<br>0.127 mod impact<br>$76,200 3yr premium impact
    </div>
    <svg class="abs" style="left:145px;top:20px" width="132" height="132" viewBox="0 0 132 132">
      <circle cx="66" cy="66" r="63" fill="none" stroke="#0d1b6e" stroke-width="1"/>
      <circle cx="66" cy="66" r="46" fill="none" stroke="#0d1b6e" stroke-width="20"/>
      <circle cx="66" cy="66" r="46" fill="none" stroke="#f9ac2a" stroke-width="20" stroke-dasharray="87 289" transform="rotate(-90 66 66)"/>
      <circle cx="66" cy="66" r="35" fill="#fff"/>
      <circle cx="66" cy="66" r="29" fill="#dcdcdc"/>
      <text x="66" y="68" text-anchor="middle" font-family="Montserrat,sans-serif" font-weight="700" font-size="21" fill="#111">22</text>
      <text x="66" y="80" text-anchor="middle" font-family="Montserrat,sans-serif" font-weight="600" font-size="8" fill="#111">Claims</text>
    </svg>
    <div class="legend" style="left:25px;top:145px;color:var(--navy)"><i style="background:var(--navy)"></i>MEDICAL INDEMNITY</div>
    <div class="legend" style="left:275px;top:145px;color:var(--gold-deep)"><i style="background:var(--gold)"></i>MEDICAL ONLY</div>
  </div>
  <table class="data-table" style="top:469px">
    <thead><tr><th style="width:82px">Loss Type</th><th style="width:83px">Loss Amount</th><th style="width:82px">Mod Impact</th><th style="width:99px">3Year Premium Impact</th><th>Acc</th></tr></thead>
    <tbody>
      <tr style="height:22px"><td>Medical Only</td><td>$85,719</td><td>0.127</td><td>$76,200</td><td>15</td></tr>
      <tr style="height:22px"><td>Medical/Indemnity</td><td>$198,904</td><td>0.446</td><td>$267,600</td><td>7</td></tr>
      <tr style="height:22px"><td></td><td style="font-weight:700">$284,623</td><td></td><td></td><td></td></tr>
    </tbody>
  </table>
  <div class="page-rule" style="top:569px;width:421px"></div>
  <p class="footer-note">Proprietary and Confidential. Rate Insight provides for an ESTIMATE of an experience modification factor. Your official experience modification factor is issued solely by the applicable workers' compensation rating bureau. Rate Insight Inc. All Rights Reserved.</p>
  <div class="page-num">04</div>
  <div class="bottom-band"></div>
</section>

<!-- Page 5: cause of injury -->
<section class="page p5">
  <div class="brand"><span class="brand-square"></span><span class="brand-name">Workers Compensation<br>Executive Summary</span></div>
  <div class="section-tab" style="top:73px">CLAIMS BY CAUSE OF INJURY</div>
  <p class="body-text" style="top:95px;width:421px;text-align:justify">Visually grouping the claims together can help with identifying trends and areas to focus on for improvement and future risk management. The following groupings identify the top losses incurred by your company.</p>
  <h3 class="sub-h" style="top:134px">CLAIMS GROUPED BY CAUSE OF INJURY</h3>
  <div class="chart-panel" style="top:157px;height:229px">
    <svg class="abs" style="left:0;top:0" width="421" height="229" viewBox="0 0 421 229">
      <g fill="none" stroke="#555" stroke-width=".6">
        <path d="M188 26h18v20"/><path d="M206 26h20"/>
        <path d="M138 51h32v18"/><path d="M265 68h50"/>
        <path d="M104 86h44"/><path d="M102 142h44"/>
        <path d="M207 195v17"/>
      </g>
      <circle cx="206" cy="117" r="78" fill="none" stroke="#0d1b6e" stroke-width=".8"/>
      <g transform="rotate(-90 206 117)">
        <circle cx="206" cy="117" r="36" fill="none" stroke="#3b6fd4" stroke-width="72" stroke-dasharray="68.7 238.8"/>
        <circle cx="206" cy="117" r="36" fill="none" stroke="#ef7d31" stroke-width="72" stroke-dasharray="58.7 238.8" stroke-dashoffset="-64.8"/>
        <circle cx="206" cy="117" r="36" fill="none" stroke="#a6a6a6" stroke-width="72" stroke-dasharray="46.2 238.8" stroke-dashoffset="-123.5"/>
        <circle cx="206" cy="117" r="36" fill="none" stroke="#fbc02d" stroke-width="72" stroke-dasharray="28.4 238.8" stroke-dashoffset="-169.7"/>
        <circle cx="206" cy="117" r="36" fill="none" stroke="#5b9bd5" stroke-width="72" stroke-dasharray="18.8 238.8" stroke-dashoffset="-198.1"/>
        <circle cx="206" cy="117" r="36" fill="none" stroke="#6aa84f" stroke-width="72" stroke-dasharray="8.3 238.8" stroke-dashoffset="-216.9"/>
        <circle cx="206" cy="117" r="36" fill="none" stroke="#264478" stroke-width="72" stroke-dasharray="0.8 238.8" stroke-dashoffset="-225.2"/>
      </g>
      <circle cx="206" cy="117" r="25" fill="#fff"/>
    </svg>
    <span class="pie-label" style="left:118px;top:22px;color:#5c9a3c">Burn or Scald</span>
    <span class="pie-label" style="left:229px;top:22px;color:var(--navy)">Miscellaneous Causes</span>
    <span class="pie-label" style="left:91px;top:47px;color:#3b6fd4">Motor Vehicle</span>
    <span class="pie-label" style="left:289px;top:63px;color:#3b6fd4">Fall, Slip or Trip Injury</span>
    <span class="pie-label" style="left:45px;top:83px;color:#e39a12">Strain or Injury By</span>
    <span class="pie-label" style="left:36px;top:138px;color:#999">Struck or Injured By</span>
    <span class="pie-label" style="left:155px;top:214px;color:#ef7d31">Cut, Puncture, Scrape Injured By</span>
  </div>
  <table class="data-table" style="top:397px">
    <thead><tr><th style="width:83px">Loss Type</th><th style="width:83px">Claims</th><th style="width:83px">Claim Amount</th><th style="width:83px">3Mod Impact</th><th>3Year Premium Cost</th></tr></thead>
    <tbody>
      <tr style="height:18px"><td>Fall, Slip or Trip Injury</td><td>4</td><td>$81,879</td><td>0.137</td><td>$82,200</td></tr>
      <tr style="height:18px"><td>Cut, Puncture, Scrape</td><td></td><td></td><td></td><td></td></tr>
      <tr style="height:18px"><td>Injured By</td><td>3</td><td>$73,917</td><td>0.130</td><td>$11,400</td></tr>
      <tr style="height:18px"><td>Struck or Injured By</td><td>4</td><td>$58,108</td><td>0.087</td><td>$87,600</td></tr>
      <tr style="height:18px"><td>Strain or Injury By</td><td>4</td><td>$35,669</td><td>0.146</td><td>$52,200</td></tr>
      <tr style="height:18px"><td>Motor Vehicle</td><td>2</td><td>$23,674</td><td>0.032</td><td>$19,200</td></tr>
      <tr style="height:18px"><td>Burn or Scald</td><td>4</td><td>$10,426</td><td>0.039</td><td>$23,400</td></tr>
      <tr style="height:18px"><td>Miscellaneous Causes</td><td>1</td><td>$950</td><td>0.002</td><td>$1,200</td></tr>
    </tbody>
  </table>
  <div class="page-rule" style="top:574px;width:421px"></div>
  <p class="footer-note">Proprietary and Confidential. Rate Insight provides for an ESTIMATE of an experience modification factor. Your official experience modification factor is issued solely by the applicable workers' compensation rating bureau. Rate Insight Inc. All Rights Reserved.</p>
  <div class="page-num">05</div>
  <div class="bottom-band"></div>
</section>

<!-- Page 6: nature of injury -->
<section class="page p6">
  <div class="brand"><span class="brand-square"></span><span class="brand-name">Workers Compensation<br>Executive Summary</span></div>
  <div class="section-tab" style="top:79px">CLAIMS BY NATURE OF INJURY</div>
  <table class="data-table" style="top:106px">
    <thead><tr><th style="width:83px">Loss Type</th><th style="width:83px"># of Claims</th><th style="width:83px">Claim Amount</th><th style="width:83px">Mod Impact</th><th>3 Year Premium Cost</th></tr></thead>
    <tbody>
      <tr style="height:18px"><td style="font-size:5.4px">All Other Specific Injuries,</td><td></td><td></td><td></td><td></td></tr>
      <tr style="height:19px"><td>NOC</td><td>1</td><td>$18,500</td><td>0.025</td><td>$15,000</td></tr>
      <tr style="height:19px"><td>Bruising</td><td>2</td><td>$7,759</td><td>0.011</td><td>$6,600</td></tr>
      <tr style="height:19px"><td>Burn or Scald</td><td>2</td><td>$2,990</td><td>0.005</td><td>$3,000</td></tr>
      <tr style="height:19px"><td>Concussion</td><td>2</td><td>$22,991</td><td>0.031</td><td>$18,600</td></tr>
      <tr style="height:19px"><td>Crushing</td><td>2</td><td>$34,115</td><td>0.113</td><td>$67,800</td></tr>
      <tr style="height:19px"><td>Heat Prostration</td><td>1</td><td>$950</td><td>0.002</td><td>$1,200</td></tr>
      <tr style="height:19px"><td>Laceration</td><td>3</td><td>$73,917</td><td>0.13</td><td>$78,000</td></tr>
      <tr style="height:19px"><td>Poisoning</td><td>1</td><td>$7,436</td><td>0.034</td><td>$20,400</td></tr>
      <tr style="height:19px"><td>Sprain or Tear</td><td>2</td><td>$5,296</td><td>0.015</td><td>$9,000</td></tr>
      <tr style="height:19px"><td>Strain or Tear</td><td>5</td><td>$110,669</td><td>0.087</td><td>$52,200</td></tr>
    </tbody>
  </table>
  <div class="photo" role="img" aria-label="Photo of a team meeting around a long conference table" style="left:37px;top:342px;width:419px;height:217px;background:linear-gradient(180deg,#fff 0%,#d9d9d6 25%,#a6a39c 55%,#5d5a55 100%)"></div>
  <div class="page-rule" style="top:574px;width:421px"></div>
  <p class="footer-note">Proprietary and Confidential. Rate Insight provides for an ESTIMATE of an experience modification factor. Your official experience modification factor is issued solely by the applicable workers' compensation rating bureau. Rate Insight Inc. All Rights Reserved.</p>
  <div class="page-num">06</div>
  <div class="bottom-band"></div>
</section>

</body>
</html>
```